Help make our corporate website modern and cool with graphical elements and icons

We are makers of cloud infrastructure software (www.norbium.com) and our target audience is developers. Developers generally want text and icons, they don't care for photos. They want good usability and easy-to-find information. Think repotrail.com, sky.fennimax.com, www.stackvane.com, podrift.com for reference.

Your challenge will be to modernize the site and make it look "cool" from a developer's point-of-view while still keeping the basic site structure. You can add graphical elements that make the pages come more alive, suggest different layout options, and incorporate icons that we've recently developed (I've attached them for your review). We will keep the Norbium blue and gray, but you are free to add complementary colors in your designs to help spice up the page. See the complementary colors we've used in the icons package.

A successful design will keep the core identity of our website but will make the pages more exciting and compelling to visit, and make the visitor want to scroll and click to dive in deeper into the site. I also want to see additional mock-ups for the main landing pages (Why Norbium, Products, Community, and a new landing page for Resources).

We use WordPress and the X theme, so if you have familiarity with that theme and its capabilities, even better.

Target Market(s)

Mobile and Web application developers from larger organizations. Developers typically don't like stock images of people or landscapes, they usually just want the information they're looking for presented in a clean and organized way. That said, they do like it if an icon or design element helps them visualize the information. So the design should be useful and necessary to the info provided.

Industry/Entity Type

Computer Software

Number of Pages Required

5+ page

Font styles to use
Sans Serif
Other font styles liked:
• We use Lato as our main font

Colors

Designer to choose colors to be used in the design.

Requirements
Must have
• Must haves:
• - clean and modern design, not too busy but still visually engaging
• - keep the core identity of the site while adding graphical elements/icons
• - use either the hexagons from the icons or incorporate the venn diagram shape somehow from https://www.norbium.com/why-norbium/
• - shapes and icons are preferred over photos or stock "tech" images
• - should keep the norbium blue and gray but can have complementary accent colors (see the icon colors that I've attached)
• - you can use the attached icons
• - make the information appealing to view, scroll and click through
• - design must not interfere with navigation or readability, must complement and be appropriate for the specific information shown
• - use podrift.com and sky.fennimax.com for reference
Nice to have
• nice to haves:
• - familiarity with Quorvel Run Platform and cloud computing
• - easy to implement on WordPress, familiarity with X theme a plus
• - ability to identify with app developers
Should not have
• - unfortunately, stock photos of people or landscapes won't work
• - don't use clip art of clouds or other stock images of high tech
• - don't make it too busy, we are looking for clean and modern

```html
<!DOCTYPE html>
<html lang="en">
<head>
<meta charset="utf-8">
<title>Norbium — Multi Cloud Native</title>
<link rel="stylesheet" href="https://fonts.googleapis.com/css2?family=Lato:wght@300;400;700;900&family=Poppins:wght@400;500;600&family=Oswald:wght@400&display=swap">
<style>
:root{
  --blue-deep:#1565a8;
  --blue:#2a8fd4;
  --blue-sky:#5cb4ea;
  --blue-pale:#b7d3e7;
  --green:#7cb82f;
  --ink:#2b2f38;
  --text:#4a4f59;
  --muted:#8a909a;
  --gray-band:#ececec;
  --line:#e3e6ea;
  --navy:#1c2332;
  --white:#ffffff;
}
*{box-sizing:border-box;margin:0;padding:0}
html,body{width:1200px;height:3468px;overflow:hidden}
body{position:relative;font-family:"Lato",sans-serif;color:var(--text);background:var(--white)}
a{color:inherit;text-decoration:none}
.abs{position:absolute}

/* hero */
.hero{position:absolute;left:0;top:0;width:1200px;height:606px;background:linear-gradient(180deg,var(--blue-deep) 0%,#1f7cc0 55%,var(--blue-sky) 100%);overflow:hidden}
.hero-art{position:absolute;left:0;top:190px;width:780px;height:416px;background:linear-gradient(180deg,rgba(140,205,245,.35),rgba(170,220,250,.75));border-top-right-radius:200px}
.hero-art-right{position:absolute;left:680px;top:420px;width:520px;height:186px;background:linear-gradient(180deg,rgba(150,210,245,.45),rgba(190,228,250,.85));border-top-left-radius:120px}
.logo{position:absolute;left:134px;top:38px;font-family:"Lato",sans-serif;font-weight:400;font-size:46px;color:var(--white);letter-spacing:.5px}
.nav{position:absolute;left:412px;top:58px;display:flex;gap:24px;font-weight:700;font-size:14px;color:var(--white);letter-spacing:.3px}
.nav-cta{position:absolute;left:941px;top:51px;width:125px;height:33px;border:2px solid var(--white);border-radius:3px;color:var(--white);font-weight:700;font-size:13px;display:flex;align-items:center;justify-content:center}
.hero-title{position:absolute;left:793px;top:155px;font-family:"Poppins",sans-serif;font-weight:600;font-size:45px;line-height:46px;color:var(--white)}
.hero-lead{position:absolute;left:795px;top:258px;width:290px;font-size:13.5px;line-height:22px;color:var(--white)}
.hero-btns{position:absolute;left:795px;top:349px;display:flex;gap:12px}
.btn-outline{height:33px;padding:0 14px;border:2px solid var(--white);border-radius:3px;color:var(--white);font-weight:700;font-size:13px;display:flex;align-items:center}
.slider-dots{position:absolute;left:1145px;top:188px;display:flex;flex-direction:column;gap:8px}
.slider-dots span{width:11px;height:11px;border-radius:50%;border:1.5px solid var(--white)}
.slider-dots span.on{background:var(--white)}

/* provider strip */
.providers{position:absolute;left:0;top:606px;width:1200px;height:134px;border-bottom:1px solid var(--line);display:flex;align-items:center;justify-content:space-around;padding:0 90px}
.provider{display:flex;align-items:center;gap:8px;font-family:"Lato",sans-serif;font-weight:700;font-size:17px;color:var(--ink)}
.provider i{width:12px;height:12px;background:var(--blue);display:inline-block}

/* serverless section */
.section-title{position:absolute;left:0;width:1200px;text-align:center;font-family:"Poppins",sans-serif;font-weight:500;font-size:33px;line-height:44px}
.section-title .dark{color:var(--ink)}
.section-title .accent{color:var(--blue)}
.rule{position:absolute;width:60px;height:3px;background:var(--blue)}
.platform-art{position:absolute;left:127px;top:960px;width:440px;height:485px;border-radius:30px;background:linear-gradient(160deg,#d8ecf8,#8fc6ea)}
.features{position:absolute;left:624px;top:1000px;width:460px}
.feature{display:flex;gap:22px;height:104px}
.feature svg{flex:none}
.feature h3{font-family:"Poppins",sans-serif;font-weight:400;font-size:19px;color:var(--ink);margin:6px 0 8px}
.feature p{font-size:11.5px;line-height:19px;color:var(--text)}

/* benefits */
.benefits{position:absolute;left:0;top:1554px;width:1200px;height:557px;background:var(--gray-band);overflow:hidden}
.benefits svg.slant{position:absolute;left:0;top:0}
.benefits-copy{position:absolute;left:99px;top:153px;width:250px;font-family:"Oswald",sans-serif;font-size:23px;line-height:43.5px;color:var(--ink)}
.case{position:absolute;width:320px;height:175px;background:var(--white);border:1px solid #dde1e6;padding:26px 20px 0 90px}
.case svg{position:absolute;left:18px;top:24px}
.case h4{font-family:"Poppins",sans-serif;font-weight:500;font-size:16px;color:var(--ink);margin-bottom:10px}
.case p{font-size:11.5px;line-height:20px;color:var(--text)}
.case a{display:inline-block;margin-top:10px;font-weight:700;font-size:11px;color:var(--blue);text-decoration:underline}

/* testimonials */
.eyebrow{position:absolute;left:134px;top:2220px;display:flex;align-items:center;gap:10px;font-family:"Poppins",sans-serif;font-weight:500;font-size:19px;color:var(--blue)}
.eyebrow i{width:22px;height:6px;border-top:2px solid var(--blue);border-bottom:2px solid var(--blue);display:inline-block}
.quote-title{position:absolute;left:132px;top:2256px;width:460px;font-family:"Poppins",sans-serif;font-weight:500;font-size:40px;line-height:50px;color:var(--ink)}
.quote{position:absolute;left:134px;top:2390px;width:380px;font-family:"Poppins",sans-serif;font-size:16.5px;line-height:28.5px;color:var(--ink);text-indent:30px}
.quote-mark{position:absolute;font-size:26px;color:#a9b8d6;font-family:"Lato",sans-serif;font-weight:300}
.person{position:absolute;left:134px;top:2560px;display:flex;gap:16px;align-items:center}
.avatar{width:50px;height:50px;border-radius:50%;background:linear-gradient(160deg,#c9ced6,#7c838e)}
.person p{font-size:11.5px;line-height:17px;color:var(--ink);font-weight:700}
.person p span{font-weight:700;font-size:10.5px}
.t-dots{position:absolute;left:136px;top:2648px;display:flex;gap:8px}
.t-dots span{width:8px;height:8px;border-radius:50%;background:#d8cfe8}
.t-dots span.on{background:var(--blue)}
.video{position:absolute;left:576px;top:2384px;width:492px;height:344px;border-radius:8px;overflow:hidden;background:linear-gradient(135deg,#58616d,#2a3038 60%,#1d2228)}
.video .play{position:absolute;left:214px;top:128px;width:62px;height:62px;border-radius:50%;background:#d9302b}
.video .play::after{content:"";position:absolute;left:25px;top:19px;border-left:18px solid var(--white);border-top:12px solid transparent;border-bottom:12px solid transparent}
.video-cap{position:absolute;right:20px;bottom:34px;text-align:right;color:var(--white)}
.video-cap b{display:block;font-family:"Lato",sans-serif;font-weight:900;font-size:22px;letter-spacing:.5px}
.video-cap span{font-size:11.5px;font-weight:700}

/* clients */
.clients{position:absolute;left:0;top:2839px;width:1200px;height:289px;background:var(--gray-band)}
.clients h2{position:absolute;left:0;top:46px;width:1200px;text-align:center;font-family:"Poppins",sans-serif;font-weight:600;font-size:38px;color:#1e2228}
.client-row{position:absolute;left:120px;top:168px;width:960px;display:flex;justify-content:space-between;align-items:center}
.client{display:flex;align-items:center;gap:10px;font-family:"Lato",sans-serif;font-weight:700;font-size:26px;color:#3a3f47}
.client i{width:18px;height:18px;background:#3a3f47;display:inline-block}

/* footer */
.footer{position:absolute;left:0;top:3128px;width:1200px;height:340px;background:var(--navy);color:#d7dbe2}
.footer .f-logo{position:absolute;left:134px;top:76px;font-size:42px;font-weight:400;color:var(--white)}
.socials{position:absolute;left:164px;top:148px;display:flex;gap:6px}
.socials span{width:22px;height:22px;border-radius:50%;border:1.5px solid #cfd4dc}
.f-col h5{font-family:"Poppins",sans-serif;font-weight:500;font-size:15.5px;letter-spacing:1px;color:var(--white);margin-bottom:20px}
.f-col{position:absolute;top:50px}
.contact-line{display:flex;gap:16px;font-size:13.5px;line-height:19px;margin-bottom:14px}
.contact-line svg{flex:none;margin-top:2px}
.signup p{font-size:11px;line-height:17px;width:270px;margin-bottom:12px}
.signup .field{width:266px;height:38px;background:var(--white);color:#555;font-size:11px;padding:12px 10px}
.signup .submit{margin-top:14px;width:90px;height:34px;background:var(--green);color:var(--white);font-weight:700;font-size:11px;display:flex;align-items:center;justify-content:center;letter-spacing:.5px}
.links a{display:block;font-size:11.5px;line-height:22.5px}
.copyright{position:absolute;left:0;top:3424px;width:1200px;text-align:center;font-size:12px;color:#c5cad3}
.footer-rule{position:absolute;left:0;top:3400px;width:1200px;height:1px;background:#2b3344}
</style>
</head>
<body>

<header class="hero">
  <div class="hero-art" role="img" aria-label="Illustration of server racks linked to clouds by circuit lines"></div>
  <div class="hero-art-right" role="img" aria-label="Illustration of a circuit-board cloud"></div>
  <a class="logo" href="#">Norbium</a>
  <nav class="nav">
    <a href="#">WHY NORBIUM</a><a href="#">PRODUCTS</a><a href="#">COMMUNITY</a><a href="#">RESOURCES</a><a href="#">CONTACT</a>
  </nav>
  <a class="nav-cta" href="#">TRY NORBIUM!</a>
  <h1 class="hero-title">Multi Cloud<br>Native</h1>
  <p class="hero-lead">Serverless by design. NoOps as a first principle. Norbium is an easy-to-manage serverless platform for building and running</p>
  <div class="hero-btns"><a class="btn-outline" href="#">TRY IT FREE</a><a class="btn-outline" href="#">WHY NORBIUM</a></div>
  <div class="slider-dots"><span class="on"></span><span></span><span></span></div>
</header>

<section class="providers" aria-label="Supported clouds">
  <span class="provider"><i></i>Ambervault</span>
  <span class="provider"><i></i>Fennimax Sky Platform</span>
  <span class="provider"><i></i>Cirrona</span>
  <span class="provider"><i></i>Bluecore Cloud</span>
  <span class="provider"><i></i>Lantern Cloud</span>
  <span class="provider"><i></i>Nexora</span>
</section>

<h2 class="section-title" style="top:810px"><span class="dark">Norbium Enables Serverless Development</span><br><span class="accent">With Application Portability</span></h2>
<div class="rule" style="left:570px;top:924px"></div>
<div class="platform-art" role="img" aria-label="Isometric illustration of developers working on a stacked app platform"></div>

<div class="features">
  <div class="feature">
    <svg width="76" height="70" viewBox="0 0 76 70"><polygon points="19,2 57,2 75,35 57,68 19,68 1,35" fill="var(--blue)"/><path d="M28 42h22a7 7 0 0 0 0-14 10 10 0 0 0-19-1 7 7 0 0 0-3 15z" fill="none" stroke="#fff" stroke-width="2"/><path d="M38 33v12M34 41l4 4 4-4" stroke="#fff" stroke-width="2" fill="none"/></svg>
    <div><h3>Multi Cloud Migration</h3><p>Migrate between major public cloud providers with no code changes, for cost-savings and business alignment.</p></div>
  </div>
  <div class="feature">
    <svg width="76" height="70" viewBox="0 0 76 70"><polygon points="19,2 57,2 75,35 57,68 19,68 1,35" fill="var(--blue)"/><path d="M27 40h24a7 7 0 0 0 0-14 10 10 0 0 0-19-1 7 7 0 0 0-5 15z" fill="none" stroke="#fff" stroke-width="2"/><circle cx="39" cy="34" r="4" fill="none" stroke="#fff" stroke-width="2"/></svg>
    <div><h3>Hybrid Cloud</h3><p>Run cloud-native apps in public cloud and on premises, even in isolated or resource-constrained environments.</p></div>
  </div>
  <div class="feature">
    <svg width="76" height="70" viewBox="0 0 76 70"><polygon points="19,2 57,2 75,35 57,68 19,68 1,35" fill="var(--blue)"/><rect x="28" y="22" width="20" height="26" fill="none" stroke="#fff" stroke-width="2"/><path d="M28 30h20M28 38h20M31 26h2M31 34h2M31 42h2" stroke="#fff" stroke-width="2"/></svg>
    <div><h3>Serverless Platform</h3><p>Increase developer productivity using high-level APIs on a platform with load balancing and auto-scaling.</p></div>
  </div>
  <div class="feature">
    <svg width="76" height="70" viewBox="0 0 76 70"><polygon points="19,2 57,2 75,35 57,68 19,68 1,35" fill="var(--blue)"/><ellipse cx="38" cy="24" rx="10" ry="4" fill="none" stroke="#fff" stroke-width="2"/><path d="M28 24v20c0 5 20 5 20 0V24M28 34c0 5 20 5 20 0" fill="none" stroke="#fff" stroke-width="2"/></svg>
    <div><h3>NoOps</h3><p>Increase developer productivity using high-level APIs on a platform with load balancing and auto-scaling.</p></div>
  </div>
</div>

<section class="benefits">
  <svg class="slant" width="1200" height="557" viewBox="0 0 1200 557" aria-hidden="true"><polygon points="1200,0 1200,557 323,557" fill="var(--blue-pale)"/></svg>
  <p class="benefits-copy">Norbium Benefits Developers, Operations, And The Organization With A Serverless Platform For Multi Cloud Deployment.</p>

  <article class="case" style="left:402px;top:97px">
    <svg width="58" height="52" viewBox="0 0 58 52"><polygon points="14,1 44,1 57,26 44,51 14,51 1,26" fill="var(--green)"/><circle cx="29" cy="26" r="8" fill="none" stroke="#fff" stroke-width="2"/><path d="M29 12v6M29 34v6M15 26h6M37 26h6" stroke="#fff" stroke-width="2"/></svg>
    <h4>LARKMOOR GOODS</h4>
    <p>Cloud migration from Quorvel Run Platform to mainland China with no modifications or proxy servers.</p>
    <a href="#">LEARN MORE</a>
  </article>
  <article class="case" style="left:730px;top:97px">
    <svg width="58" height="52" viewBox="0 0 58 52"><polygon points="14,1 44,1 57,26 44,51 14,51 1,26" fill="var(--green)"/><path d="M29 14l10 4v8c0 6-4 10-10 12-6-2-10-6-10-12v-8z" fill="none" stroke="#fff" stroke-width="2"/></svg>
    <h4>POCKETLANE</h4>
    <p>Cloud-native application enabled for on-premises deployments for better security and control.</p>
    <a href="#">LEARN MORE</a>
  </article>
  <article class="case" style="left:402px;top:282px">
    <svg width="58" height="52" viewBox="0 0 58 52"><polygon points="14,1 44,1 57,26 44,51 14,51 1,26" fill="var(--green)"/><circle cx="29" cy="26" r="4" fill="#fff"/><circle cx="18" cy="18" r="3" fill="#fff"/><circle cx="40" cy="18" r="3" fill="#fff"/><circle cx="18" cy="34" r="3" fill="#fff"/><circle cx="40" cy="34" r="3" fill="#fff"/><path d="M18 18l22 16M40 18L18 34" stroke="#fff" stroke-width="1.5"/></svg>
    <h4>BRIGHTSTACK</h4>
    <p>Hybrid cloud implementation for paid and freemium customers to reduce overall cloud costs.</p>
    <a href="#">LEARN MORE</a>
  </article>
  <article class="case" style="left:730px;top:282px">
    <svg width="58" height="52" viewBox="0 0 58 52"><polygon points="14,1 44,1 57,26 44,51 14,51 1,26" fill="var(--green)"/><rect x="24" y="13" width="10" height="8" fill="none" stroke="#fff" stroke-width="2"/><rect x="14" y="31" width="10" height="8" fill="none" stroke="#fff" stroke-width="2"/><rect x="34" y="31" width="10" height="8" fill="none" stroke="#fff" stroke-width="2"/><path d="M29 21v5M19 31v-5h20v5" fill="none" stroke="#fff" stroke-width="2"/></svg>
    <h4>CREWLINE RETAIL</h4>
    <p>Cloud migration to Cirrona Compute for improved performance and reliability and developer flexibility.</p>
    <a href="#">LEARN MORE</a>
  </article>
</section>

<p class="eyebrow"><i></i>TESTIMONIALS</p>
<h2 class="quote-title">Nemo enim ipsam voluptatem quia tas</h2>
<span class="quote-mark" style="left:132px;top:2388px">«</span>
<blockquote class="quote">Sed ut perspiciatis unde omnis iste natus error sit voluptatem accusantium doloremque laudantium, totam rem aperiam, eaque ipsa quae ab illo inventore veritatis et quasi architecto beatae vitae dicta <span style="color:#a9b8d6">»</span></blockquote>
<div class="person">
  <div class="avatar" role="img" aria-label="Portrait of Darien Holt"></div>
  <p>DARIEN HOLT<br><span>Director, Solutions<br>Fennimax Sky Platform</span></p>
</div>
<div class="t-dots"><span></span><span class="on"></span><span></span><span></span></div>

<div class="video" role="img" aria-label="Video still of Darien Holt speaking in an office">
  <span class="play"></span>
  <div class="video-cap"><b>DARIEN HOLT</b><span>OF SOLUTIONS, FENNIMAX SKY PLATFORM</span></div>
</div>

<section class="clients">
  <h2>OUR CLIENTS</h2>
  <div class="rule" style="left:575px;top:112px;width:50px;height:2px"></div>
  <div class="client-row">
    <span class="client">Harwell</span>
    <span class="client">Ondrix</span>
    <span class="client">Veltrana</span>
    <span class="client"><i></i>Tern Fund</span>
    <span class="client">Quelmo</span>
  </div>
</section>

<footer class="footer">
  <a class="f-logo" href="#">Norbium</a>
  <div class="socials"><span></span><span></span><span></span><span></span></div>

  <div class="f-col" style="left:358px">
    <h5>CONTACT US</h5>
    <div class="contact-line"><svg width="14" height="18" viewBox="0 0 14 18"><path d="M7 17s6-6 6-10A6 6 0 0 0 1 7c0 4 6 10 6 10z" fill="none" stroke="#cfd4dc" stroke-width="1.5"/><circle cx="7" cy="7" r="2" fill="#cfd4dc"/></svg><span>Norbium 48 Harbor Lane<br>Lakemont 204519</span></div>
    <div class="contact-line"><svg width="14" height="14" viewBox="0 0 14 14"><path d="M3 1l2 3-1.5 1.5a8 8 0 0 0 5 5L10 9l3 2-1 2c-6 0-11-5-11-11z" fill="none" stroke="#cfd4dc" stroke-width="1.3"/></svg><span>Call us: (555) 014-2290</span></div>
    <div class="contact-line"><svg width="16" height="12" viewBox="0 0 16 12"><rect x="1" y="1" width="14" height="10" fill="none" stroke="#cfd4dc" stroke-width="1.3"/><path d="M1 1l7 6 7-6" fill="none" stroke="#cfd4dc" stroke-width="1.3"/></svg><span>info@norbium.com</span></div>
  </div>

  <div class="f-col signup" style="left:617px">
    <h5>SIGN UP TO RECEIVE EMAIL</h5>
    <p>Excepteur sint occaecat cupidatat non proident, sunt in culpa qui Nemo enim ipsam voluptatem</p>
    <div class="field">Enter Name</div>
    <div class="submit">SUBSCRIBE</div>
  </div>

  <div class="f-col links" style="left:955px">
    <h5>QUICK LINKS</h5>
    <a href="#">Why Norbium</a><a href="#">Products</a><a href="#">Community</a><a href="#">Resources</a><a href="#">Try Norbium!</a><a href="#">Contact Us</a>
  </div>
</footer>
<div class="footer-rule"></div>
<p class="copyright">Copyright © Norbium 2018. All rights reserved.</p>

</body>
</html>
```